American cannabis tech company business card design

Thrum.com is seeking a modern, professional, and brand-aligned business card that represents our company and its core values: Mission, Story, Values, and Impact. As an innovative cannabis company, we want a business card that is not only visually appealing but also serves as a representation of who we are and what we stand for.

Project Scope: Design a double-sided business card that integrates our brand identity and core values. Incorporate our key brand elements, ensuring a sleek and contemporary aesthetic. Visually reflect our core values (Mission, Story, Values, Impact) in a way that is engaging yet professional.

Target Market(s)

Vendors, third parties,

Contact Information for Business Card

Contact details (name, title, email, phone, website, etc.)

Font styles to use
Other font styles liked:
• Caslon, Centra

Colors

Designer to choose colors to be used in the design.

Requirements
Must have
• Thrum.com logo and branding A creative yet clean way to integrate our core values (Mission, Story, Values, Impact) Modern typography and a well-structured layout
Nice to have
• forest green, grey, white, black
Should not have
• references to marijuana, leafs, plants, or related product

```html
<!DOCTYPE html>
<html lang="en">
<head>
<meta charset="utf-8">
<title>Thrum.com Business Card</title>
<link href="https://fonts.googleapis.com/css2?family=Libre+Caslon+Text:wght@400;700&display=swap" rel="stylesheet">
<style>
  :root {
    --backdrop: #a9a9a9;
    --forest: #1b3320;
    --paper: #ffffff;
    --mist: #eef1ee;
    --ink: #1b3320;
  }
  html, body {
    margin: 0;
    padding: 0;
    width: 1199px;
    height: 1200px;
    overflow: hidden;
    background: var(--backdrop);
  }
  .canvas {
    position: relative;
    width: 1199px;
    height: 1200px;
  }
  .card {
    position: absolute;
    left: 147px;
    width: 905px;
    height: 528px;
    box-shadow: 0 4px 12px rgba(0,0,0,0.35);
    overflow: hidden;
  }
  .card-front { top: 55px; background: var(--paper); }
  .card-back { top: 616px; background: var(--forest); }

  .wordmark {
    font-family: "Libre Caslon Text", serif;
    font-weight: 700;
    letter-spacing: -2px;
    line-height: 1;
    margin: 0;
  }
  .card-front .wordmark {
    position: absolute;
    right: 71px;
    top: 58px;
    font-size: 98px;
    color: var(--ink);
  }
  .card-back .wordmark {
    position: absolute;
    left: 0;
    right: 0;
    top: 218px;
    text-align: center;
    font-size: 120px;
    color: var(--paper);
  }

  .emblem-fill {
    position: absolute;
    left: 420px;
    top: 130px;
    width: 485px;
    height: 398px;
    background: radial-gradient(ellipse at 62% 70%, var(--mist) 0%, rgba(238,241,238,0.6) 45%, rgba(255,255,255,0) 72%);
  }

  .identity {
    position: absolute;
    left: 75px;
    top: 252px;
    font-family: "Libre Caslon Text", serif;
    color: var(--ink);
  }
  .identity .name {
    margin: 0;
    font-size: 31px;
    font-weight: 700;
    letter-spacing: 0.5px;
    line-height: 1;
  }
  .identity .title {
    margin: 12px 0 0;
    font-size: 20px;
    font-weight: 400;
  }

  .contact-list {
    position: absolute;
    left: 75px;
    top: 366px;
    margin: 0;
    padding: 0;
    list-style: none;
    font-family: "Libre Caslon Text", serif;
    font-size: 19px;
    color: var(--ink);
  }
  .contact-list li {
    display: flex;
    align-items: center;
    height: 35px;
  }
  .contact-list svg {
    width: 18px;
    height: 18px;
    margin-right: 19px;
    fill: var(--ink);
  }
</style>
</head>
<body>
<main class="canvas">
  <section class="card card-front">
    <div class="emblem-fill" role="img" aria-label="Faint decorative brand emblem"></div>
    <h1 class="wordmark">THRUM</h1>
    <div class="identity">
      <p class="name">DALTON REEVE</p>
      <p class="title">Owner</p>
    </div>
    <ul class="contact-list">
      <li>
        <svg viewBox="0 0 18 18" aria-hidden="true"><path d="M5 1h8a1 1 0 0 1 1 1v14a1 1 0 0 1-1 1H5a1 1 0 0 1-1-1V2a1 1 0 0 1 1-1zm1 2v10h6V3zm3 11.2a.9.9 0 1 0 0 1.8.9.9 0 0 0 0-1.8z"/></svg>
        <span>555-014-7392</span>
      </li>
      <li>
        <svg viewBox="0 0 18 18" aria-hidden="true"><path d="M2 4h14v10H2zM2.6 4.6 9 9.4l6.4-4.8v1.6L9 11 2.6 6.2z" fill-rule="evenodd"/></svg>
        <span>d@reevestudio.tech</span>
      </li>
      <li>
        <svg viewBox="0 0 18 18" aria-hidden="true"><path d="M9 2a7 7 0 1 0 0 14A7 7 0 0 0 9 2zm0 1.6c.8 0 1.8 1.6 2.1 4.4H6.9C7.2 5.2 8.2 3.6 9 3.6zM3.7 8h1.7c0-1.5.4-2.9.9-3.8A5.4 5.4 0 0 0 3.7 8zm0 2a5.4 5.4 0 0 0 2.6 3.8c-.5-.9-.8-2.3-.9-3.8zm3.2 0c.3 2.8 1.3 4.4 2.1 4.4s1.8-1.6 2.1-4.4zm5.7 0c-.1 1.5-.4 2.9-.9 3.8A5.4 5.4 0 0 0 14.3 10zm1.7-2a5.4 5.4 0 0 0-2.6-3.8c.5.9.8 2.3.9 3.8z"/></svg>
        <span>www.reevestudio.tech</span>
      </li>
    </ul>
  </section>

  <section class="card card-back">
    <p class="wordmark">THRUM</p>
  </section>
</main>
</body>
</html>
```